Geothermal company needs a creative "POW" business card

Manufacturers tend to be boring. We are not! We are a Geothermal Heat Pump company that has over 30 yrs of experience and wants a new look and updated feel. Nothing old (yawn) so get your creative hats on and let's rock!

We want to use the great colors of lime green and navy blue. Our new logo is attached and we're ready to roll. Remember, we're a professional leader in the geothermal industry that needs to make an eye catching and memorable first glance.

```html
<!DOCTYPE html>
<html lang="en">
<head>
<meta charset="utf-8">
<title>Boreal Thermal Business Cards</title>
<link href="https://fonts.googleapis.com/css2?family=Encode+Sans+Semi+Condensed:wght@400;600&family=Arimo:wght@400;700&display=swap" rel="stylesheet">
<style>
  :root {
    --navy: #0b2340;
    --lime: #7ab51d;
    --paper: #ffffff;
    --ink: #1b2a3d;
  }
  html, body { margin: 0; padding: 0; overflow: hidden; }
  body { width: 1200px; height: 1000px; background: var(--paper); position: relative; }
  .card { position: absolute; background: var(--paper); box-shadow: 0 0 0 1px #eef0f3; }
  .bar { position: absolute; }
  .navy { background: var(--navy); }
  .lime { background: var(--lime); }
  .brand { position: absolute; display: flex; align-items: flex-start; }
  .brand-dot { border-radius: 50%; background: var(--navy); flex: none; }
  .brand-name { font-family: "Encode Sans Semi Condensed", sans-serif; font-weight: 600; color: var(--lime); line-height: 1; white-space: nowrap; }
  .tagline { font-family: "Encode Sans Semi Condensed", sans-serif; font-weight: 400; color: var(--navy); white-space: nowrap; line-height: 1; }
  .web { position: absolute; font-family: "Arimo", sans-serif; font-size: 13px; color: var(--ink); right: 22px; top: 177px; }
  .person { position: absolute; right: 18px; top: 20px; font-family: "Arimo", sans-serif; color: var(--navy); }
  .person-name { font-size: 14px; font-weight: 700; line-height: 1; white-space: nowrap; }
  .person-role { font-size: 9px; margin-top: 3px; }
  .contact { position: absolute; font-family: "Arimo", sans-serif; font-size: 10px; color: var(--ink); white-space: nowrap; line-height: 1; }
  .icon { position: absolute; }
</style>
</head>
<body>

  <section class="card card-front" style="left:303px; top:272px; width:360px; height:211px;">
    <div class="bar navy" style="left:0; top:0; width:280px; height:9px;"></div>
    <div class="bar lime" style="left:284px; top:0; width:76px; height:9px;"></div>
    <div class="bar lime" style="left:349px; top:0; width:11px; height:75px;"></div>
    <div class="bar navy" style="left:349px; top:80px; width:11px; height:23px;"></div>
    <div class="bar lime" style="left:349px; top:108px; width:11px; height:22px;"></div>
    <div class="bar navy" style="left:349px; top:134px; width:11px; height:77px;"></div>
    <div class="bar navy" style="left:0; top:201px; width:360px; height:10px;"></div>

    <div class="brand" style="left:18px; top:22px;">
      <div class="brand-dot" style="width:54px; height:54px;"></div>
      <div style="margin-left:13px; margin-top:7px;">
        <div class="brand-name" style="font-size:32px;">Boreal Thermal</div>
        <div class="tagline" style="font-size:9px; margin-top:3px;">Manufacturer of Geothermal Heat Pumps for the North</div>
      </div>
    </div>

    <div class="web">www.borealthermal.com</div>
  </section>

  <section class="card card-back" style="left:553px; top:518px; width:364px; height:213px;">
    <div class="bar navy" style="left:0; top:0; width:227px; height:8px;"></div>
    <div class="bar lime" style="left:232px; top:0; width:22px; height:8px;"></div>
    <div class="bar navy" style="left:258px; top:0; width:24px; height:8px;"></div>
    <div class="bar lime" style="left:286px; top:0; width:78px; height:8px;"></div>
    <div class="bar lime" style="left:352px; top:0; width:12px; height:76px;"></div>
    <div class="bar navy" style="left:352px; top:80px; width:12px; height:133px;"></div>
    <div class="bar navy" style="left:0; top:201px; width:364px; height:12px;"></div>

    <div class="brand" style="left:17px; top:20px;">
      <div class="brand-dot" style="width:28px; height:28px;"></div>
      <div style="margin-left:6px; margin-top:5px;">
        <div class="brand-name" style="font-size:17px;">Boreal Thermal</div>
        <div class="tagline" style="font-size:5px; margin-top:2px;">Manufacturer of Geothermal Heat Pumps for the North</div>
      </div>
    </div>

    <div class="person">
      <div class="person-name">Reid Halvorsen</div>
      <div class="person-role">CEO</div>
    </div>

    <svg class="icon" style="left:55px; top:133px;" width="8" height="10" viewBox="0 0 8 10" aria-hidden="true">
      <path d="M4 0a4 4 0 0 1 4 4c0 2.5-4 6-4 6S0 6.5 0 4a4 4 0 0 1 4-4z" fill="var(--lime)"/>
      <circle cx="4" cy="4" r="1.4" fill="#fff"/>
    </svg>
    <div class="contact" style="left:73px; top:134px;">48 N Birch Ave</div>
    <div class="contact" style="left:74px; top:155px;">Lakeview, MN 56300</div>

    <svg class="icon" style="left:55px; top:176px;" width="11" height="8" viewBox="0 0 11 8" aria-hidden="true">
      <rect x="0.5" y="0.5" width="10" height="7" fill="none" stroke="var(--lime)"/>
      <path d="M0.5 0.5 5.5 4.5 10.5 0.5" fill="none" stroke="var(--lime)"/>
    </svg>
    <div class="contact" style="left:74px; top:176px;">reidhalvorsen@borealthermal.com</div>

    <svg class="icon" style="left:208px; top:131px;" width="13" height="11" viewBox="0 0 13 11" aria-hidden="true">
      <rect x="3" y="0" width="7" height="4" fill="var(--lime)"/>
      <rect x="0" y="4" width="13" height="5" fill="var(--lime)"/>
      <rect x="3" y="7" width="7" height="4" fill="var(--lime)"/>
      <rect x="4" y="8" width="5" height="2" fill="#fff"/>
    </svg>
    <div class="contact" style="left:230px; top:134px;">(555) 214-3100</div>

    <svg class="icon" style="left:212px; top:153px;" width="7" height="11" viewBox="0 0 7 11" aria-hidden="true">
      <path d="M2 0h2l0.5 3-1.5 1c0 1 0.5 2.5 1.5 3l1.5-1 1 2.5-1.5 2C2 10 0 6 0 3z" fill="var(--lime)"/>
    </svg>
    <div class="contact" style="left:230px; top:155px;">(555) 214-3101</div>
  </section>

</body>
</html>
```